Personal Training

Personal Fitness Trainer
Sports Nutritionist
Individual and Group rates available
Certifications
Global Wellness Coaches Federation
Worldwide Athletic Study Council

Industry/Entity Type

Fitness

Contact Information for Business Card

Dorinda Valcourt
555-284-7160
dvalcourt4@brimfeld.com

```html
<!DOCTYPE html>
<html lang="en">
<head>
<meta charset="utf-8">
<title>Dorinda Valcourt – Personal Training Business Card</title>
<link rel="stylesheet" href="https://fonts.googleapis.com/css2?family=Questrial&family=Italianno&display=swap">
<style>
  :root {
    --page-bg: #ece9ee;
    --card-white: #ffffff;
    --card-grey: #f1f0f3;
    --purple: #9b7fcf;
    --purple-deep: #8a6cc2;
    --purple-soft: #c4b2e4;
    --ink: #2c2a30;
    --photo-dark: #6f6a80;
    --photo-light: #c9c5d3;
    --badge-red: #d8424a;
    --badge-blue: #2c4fa3;
  }
  * { box-sizing: border-box; margin: 0; padding: 0; }
  html, body { width: 1200px; height: 1000px; overflow: hidden; }
  body {
    background: var(--page-bg);
    font-family: "Questrial", sans-serif;
    position: relative;
  }
  .card {
    position: absolute;
    overflow: hidden;
    border-radius: 4px;
    box-shadow: 0 10px 28px rgba(40, 30, 60, 0.18);
  }

  /* Back of card: credentials */
  .card-back {
    left: 50px; top: 320px;
    width: 630px; height: 360px;
    background: linear-gradient(180deg, var(--card-white) 0%, var(--card-grey) 100%);
  }
  .card-back .titles {
    position: absolute;
    left: 36px; top: 26px;
    color: var(--purple);
    font-size: 31px;
    line-height: 1.15;
  }
  .card-back .titles span { display: block; }
  .card-back .titles span:nth-child(2) { padding-left: 36px; }
  .card-back .titles span:nth-child(3) { padding-left: 72px; }
  .card-back .trainer-photo {
    position: absolute;
    left: 0; top: 138px;
    width: 232px; height: 222px;
    background: linear-gradient(160deg, var(--photo-light) 0%, var(--photo-dark) 55%, #8e88a0 100%);
  }
  .card-back .cert-band {
    position: absolute;
    left: 232px; top: 150px;
    width: 398px; height: 44px;
    background: var(--purple);
    color: #fff;
    font-size: 24px;
    line-height: 44px;
    padding-left: 28px;
  }
  .card-back .cert-band::before {
    content: "";
    position: absolute;
    left: -232px; top: -18px;
    width: 630px; height: 4px;
    background: var(--purple-soft);
    opacity: 0;
  }
  .card-back .cert-list {
    position: absolute;
    left: 262px; top: 214px;
    font-size: 15px;
    line-height: 1.35;
    color: var(--ink);
  }
  .card-back .badges {
    position: absolute;
    left: 262px; top: 272px;
    display: flex;
    gap: 60px;
    align-items: center;
  }
  .badge { display: block; }

  /* Front of card: name and contact */
  .card-front {
    left: 760px; top: 185px;
    width: 360px; height: 630px;
    background: linear-gradient(170deg, #dcdbe0 0%, #b9b6c2 100%);
  }
  .card-front .front-photo {
    position: absolute;
    inset: 0;
    background: linear-gradient(170deg, #e4e3e8 0%, #c2bfc9 45%, #8d7d8e 70%, #3b3650 100%);
  }
  .card-front .header-arc {
    position: absolute;
    left: 0; top: 0;
    width: 360px; height: 200px;
  }
  .card-front .contact {
    position: absolute;
    left: 0; top: 22px;
    width: 360px;
    text-align: center;
    color: #fff;
  }
  .card-front .name {
    font-family: "Italianno", cursive;
    font-size: 60px;
    line-height: 1;
    letter-spacing: 1px;
  }
  .card-front .phone,
  .card-front .email {
    font-size: 19px;
    letter-spacing: 0.5px;
    line-height: 1.35;
  }
</style>
</head>
<body>

  <section class="card card-back" aria-label="Business card back">
    <h2 class="titles">
      <span>Personal Fitness</span>
      <span>Trainer</span>
      <span>Sports Nutritionist</span>
    </h2>
    <div class="trainer-photo" role="img" aria-label="Black-and-white photo of a trainer lifting dumbbells in a gym, tinted purple"></div>
    <div class="cert-band">Certifications</div>
    <p class="cert-list">
      Global Wellness Coaches Federation<br>
      Worldwide Athletic Study Council
    </p>
    <div class="badges">
      <svg class="badge" width="80" height="60" viewBox="0 0 80 60" aria-label="Federation certification badge" role="img">
        <rect x="4" y="8" width="72" height="44" rx="4" fill="none" stroke="#333" stroke-width="2"/>
      </svg>
      <svg class="badge" width="150" height="60" viewBox="0 0 150 60" aria-label="Council certification badge" role="img">
        <rect x="4" y="10" width="70" height="40" fill="var(--badge-red)"/>
        <rect x="80" y="10" width="66" height="40" fill="var(--badge-blue)"/>
      </svg>
    </div>
  </section>

  <section class="card card-front" aria-label="Business card front">
    <div class="front-photo" role="img" aria-label="Photo of a fit athlete posing with hands behind head outdoors"></div>
    <svg class="header-arc" viewBox="0 0 360 200" aria-hidden="true">
      <path d="M0 0 H360 V150 Q180 212 0 150 Z" fill="#ffffff" opacity="0.85"/>
      <path d="M0 0 H360 V140 Q180 200 0 140 Z" fill="var(--purple)"/>
    </svg>
    <div class="contact">
      <h1 class="name">Dorinda Valcourt</h1>
      <p class="phone">555-284-7160</p>
      <p class="email">dvalcourt4@brimfeld.com</p>
    </div>
  </section>

</body>
</html>
```